Creative designer wanted for unique pet treats product packaging!

My company is "Barkwell Crisp!" and we're a new and upcoming premium pet treat company. We are different than the rest as we have core values that really stand out and that we're VERY passionate about. They are the following:
HEALTHY-All of our ingredients are fresh and wholesome for dogs. Each has unique health benefits for dogs and there is never any filler-just the good stuff.
AMOUNT OF INGREDIENTS-Most of dog treats have large lists of ingredients and often many of those are difficult to pronounce or people have to look up what they even are. Often there is lot of "filler". We pride ourselves on just having a few ingredients or less. Every ingredient can easily be pronounced, recognized and are commonly consumed by humans in regular meals.
GIVING BACK- We donate a portion of the proceeds of every bag to go to hand selected, accredited and legit animals charities and rescues.
ENVIRONMENT- We strongly care about the environment which is why our bags are compostable. Just simply remove the zipper and track then put the bag in a composting bin. Easy as that. (We have attached a "how to compost your bag in 2 simple steps" image that we would like shown on the bags.
Our initial product is Cinnamon Basil Apple Bark-ley Bites. The ingredients are: Coconut oil, dill, and sweet potato.
We want a design that embodies our values. As well, we have attached "our story" that describes the company and what we are about to consumers. We would like to have it put on the package, but if it cannot be done, then just the meat and potatoes of the message.
A good example for recognition is the attached cake mix as it's simple, portrays the product nicely and when seen from afar-it is easily identified.
*We would like to have a window on the bag that is similar to our paw and leaf logo.
We would also like to see the color green on the package.
Bag specifics are:
Size: 250g OPTIMIZED
Dimensions Inches: 6.15''x9.41''x3.50''
Dimensions mm : 156x239x89
Type: Stand-Up Pouch with Zip (PLOW)
COMPOSTABLE
Material: 100NK MATTE/70NKA/3mil BIOPBS
CMYKW

```html
<!DOCTYPE html>
<html lang="en">
<head>
<meta charset="utf-8">
<title>Barkwell Crisp! – Dog Treat Pouch</title>
<link rel="stylesheet" href="https://fonts.googleapis.com/css2?family=Amatic+SC:wght@700&family=Roboto:wght@700&display=swap">
<style>
  :root {
    --page: #eeeeee;
    --orange: #f29a2e;
    --green: #6cc240;
    --green-ink: #5cb82c;
    --brown: #4a2e1a;
    --white: #ffffff;
    --window: #cfcfcf;
    --dog: #c98b3c;
  }
  * { margin: 0; padding: 0; box-sizing: border-box; }
  html, body { width: 1200px; height: 1200px; overflow: hidden; background: var(--page); }
  .pouch {
    position: absolute; left: 282px; top: 48px;
    width: 636px; height: 1104px;
    background: var(--green);
    border-radius: 10px;
    overflow: hidden;
    font-family: "Amatic SC", cursive;
  }
  .pouch-art { position: absolute; inset: 0; }
  .brand {
    position: absolute; left: 70px; top: 300px;
    display: flex; align-items: center; gap: 10px;
  }
  .brand-dot { width: 26px; height: 26px; border-radius: 50%; background: var(--brown); }
  .brand-name {
    font-family: "Roboto", sans-serif; font-weight: 700;
    font-size: 36px; color: var(--brown); letter-spacing: -1px;
  }
  .headline {
    position: absolute; left: 140px; top: 470px; width: 370px;
    text-align: center; color: var(--green-ink);
    font-size: 92px; line-height: 1; transform: rotate(-4deg);
  }
  .product-window {
    position: absolute; left: 222px; top: 588px; width: 200px; height: 126px;
    background: var(--window); border-radius: 40px;
  }
  .flavour {
    position: absolute; left: 150px; top: 718px; width: 370px;
    text-align: center; color: var(--green-ink);
    font-size: 34px; line-height: 1; transform: rotate(-5deg);
  }
  .tagline {
    position: absolute; left: 205px; top: 800px; width: 272px; height: 92px;
    background: var(--orange); border-radius: 40px;
    color: var(--white); font-size: 72px; line-height: 92px; text-align: center;
    transform: rotate(-4deg);
  }
  .audience {
    position: absolute; left: 432px; top: 872px;
    color: var(--orange); font-size: 24px; transform: rotate(-18deg);
  }
  .mascot {
    position: absolute; left: 70px; top: 740px; width: 140px; height: 240px;
    background: var(--dog); border-radius: 60px 60px 30px 30px;
  }
  .weight {
    position: absolute; left: 0; right: 0; top: 955px;
    text-align: center; color: var(--white); font-size: 56px; line-height: 1;
  }
  .giving {
    position: absolute; left: 0; right: 0; top: 1025px;
    text-align: center; color: var(--white); font-size: 22px; line-height: 1.05;
  }
</style>
</head>
<body>
  <main class="pouch">
    <svg class="pouch-art" viewBox="0 0 636 1104" width="636" height="1104" aria-hidden="true">
      <path class="top-band" d="M0,0 H636 V130 C470,300 250,410 0,410 Z" fill="var(--orange)"/>
      <path class="speech-bubble" d="M160,440 C260,420 430,425 500,450 C545,470 540,600 530,760 C522,880 500,940 470,955 L455,1000 L415,958 C320,965 180,955 140,920 C105,880 100,700 115,560 C122,480 130,450 160,440 Z" fill="var(--white)"/>
      <g role="img" aria-label="Decorative quote marks">
        <ellipse cx="70" cy="445" rx="22" ry="28" fill="#f4f4f4"/>
        <ellipse cx="115" cy="460" rx="22" ry="28" fill="#f4f4f4"/>
        <ellipse cx="520" cy="935" rx="22" ry="28" fill="#f4f4f4"/>
        <ellipse cx="565" cy="925" rx="22" ry="28" fill="#f4f4f4"/>
      </g>
    </svg>

    <div class="brand">
      <span class="brand-dot"></span>
      <span class="brand-name">Barkwell Crisp!</span>
    </div>

    <h1 class="headline">-Dog Treat-</h1>
    <div class="product-window" role="img" aria-label="Clear window showing the treats inside"></div>
    <p class="flavour">Cinnamon Basil Apple<br>Bark-ley Bites</p>
    <p class="tagline">WHOLESOME</p>
    <p class="audience">For Dogs</p>
    <div class="mascot" role="img" aria-label="Illustration of a sitting cartoon dog"></div>
    <p class="weight">250g</p>
    <p class="giving">Portion of proceeds go to<br>local animal shelter</p>
  </main>
</body>
</html>
```